Marisa Dee Creations & Affairs business card

I need an elegant informative but not busy business card using my logo. We are a florist with high end customers. I am adding a PDF file and a PNG file for those who requested it

Reason: still working on changes

Reason: Working on changes

Reason: making changes

Target Market(s)

Brides, grooms, men purchasing flowers
Ages 20-65

Industry/Entity Type

Florist

Requirements
Must have
• Business info:
Marisa Dee Creation & Affairs
www.marisadeeaffairs.example.
555-418-7362

555-418-7362
Nice to have
• Est 1954
may want Pinterest logo, twitter and linkedin and facbook
Should not have
• Clip art or photos

```html
<!DOCTYPE html>
<html lang="en">
<head>
<meta charset="utf-8">
<title>Marisa Dee Creations &amp; Affairs — Business Card</title>
<link rel="stylesheet" href="https://fonts.googleapis.com/css2?family=Cinzel:wght@400&family=Lobster&family=Marcellus&family=Parisienne&display=swap">
<style>
  :root {
    --backdrop: #2b2b2d;
    --card: #f4f3f4;
    --card-shade: #e6e5e7;
    --arc: rgba(255,255,255,0.55);
    --ink: #1c1c1c;
    --blush: #f0a9b6;
    --blush-soft: rgba(240,169,182,0.28);
    --blush-faint: rgba(240,169,182,0.16);
  }
  * { margin: 0; padding: 0; box-sizing: border-box; }
  html, body { width: 1200px; height: 900px; overflow: hidden; }
  body {
    background: var(--backdrop);
    display: flex; flex-direction: column; align-items: center; justify-content: center;
    gap: 40px;
  }
  .card {
    position: relative;
    width: 640px; height: 366px;
    background: linear-gradient(160deg, var(--card) 40%, var(--card-shade));
    overflow: hidden;
    box-shadow: 0 12px 30px rgba(0,0,0,0.5);
  }
  .card__arc {
    position: absolute; border-radius: 50%;
    background: var(--arc);
  }
  /* Front */
  .card--front .card__arc { width: 560px; height: 560px; left: 150px; top: 30px; }
  .front__wordmark {
    position: absolute; left: 0; right: 0; top: 140px; text-align: center;
  }
  .front__name {
    font-family: "Cinzel", serif; font-size: 50px; letter-spacing: 10px;
    color: var(--ink);
  }
  .front__tagline {
    font-family: "Cinzel", serif; font-size: 14px; letter-spacing: 7px;
    color: var(--blush); margin-top: 6px;
  }
  /* Back */
  .card--back .card__arc { width: 600px; height: 600px; left: 330px; top: -20px; }
  .ornament { position: absolute; }
  .ornament--main {
    left: 70px; top: 60px; width: 240px; height: 240px; border-radius: 50%;
    background: radial-gradient(circle, var(--blush-soft) 30%, var(--blush-faint) 62%, transparent 72%);
  }
  .ornament--corner {
    width: 130px; height: 130px; border-radius: 50%;
    background: radial-gradient(circle, var(--blush-faint) 40%, transparent 70%);
  }
  .ornament--tl { left: -40px; top: -20px; }
  .ornament--tr { right: -30px; top: -40px; }
  .ornament--bl { left: 20px; bottom: -50px; }
  .ornament--br { right: -30px; bottom: 40px; }
  .back__mark {
    position: absolute; left: 70px; top: 150px; width: 240px; text-align: center;
    font-family: "Cinzel", serif; font-size: 30px; color: var(--ink);
  }
  .back__details {
    position: absolute; right: 50px; top: 105px; text-align: right;
  }
  .back__name { font-family: "Lobster", cursive; font-size: 44px; color: var(--ink); line-height: 1; }
  .back__tagline { font-family: "Lobster", cursive; font-size: 18px; color: var(--blush); margin-top: 4px; }
  .back__phone { font-family: "Marcellus", serif; font-size: 25px; color: var(--blush); margin-top: 6px; letter-spacing: 1px; }
  .back__web { font-family: "Parisienne", cursive; font-size: 26px; color: var(--blush); }
  .back__social { display: flex; justify-content: flex-end; gap: 8px; margin-top: 22px; }
  .back__social span { width: 14px; height: 14px; border-radius: 50%; background: var(--blush); }
</style>
</head>
<body>
  <section class="card card--front">
    <div class="card__arc"></div>
    <div class="front__wordmark">
      <div class="front__name">Marisa Dee</div>
      <div class="front__tagline">CREATIONS &amp; AFFAIRS</div>
    </div>
  </section>

  <section class="card card--back">
    <div class="card__arc"></div>
    <div class="ornament ornament--corner ornament--tl" role="img" aria-label="faint pink floral scroll ornament"></div>
    <div class="ornament ornament--corner ornament--tr" role="img" aria-label="faint pink floral scroll ornament"></div>
    <div class="ornament ornament--corner ornament--bl" role="img" aria-label="faint pink floral scroll ornament"></div>
    <div class="ornament ornament--corner ornament--br" role="img" aria-label="faint pink floral scroll ornament"></div>
    <div class="ornament ornament--main" role="img" aria-label="pink tulip and scroll ornament around the monogram"></div>
    <div class="back__mark">Marisa Dee</div>
    <div class="back__details">
      <div class="back__name">Marisa Dee</div>
      <div class="back__tagline">Creation &amp; Affairs</div>
      <div class="back__phone">T: 555-418-7362</div>
      <div class="back__web">www.marisadeeaffairs.example</div>
      <div class="back__social" aria-label="social links">
        <span></span><span></span><span></span><span></span>
      </div>
    </div>
  </section>
</body>
</html>
```